A powerful and attractive professional-looking signage

We need a signage for the office at the door entrance. We are a professional advisory firm that serve corporate clients; hence the signage should concur an image of professionalism and sophistication. We have the logo and the Company's Motto. We are looking at having an elegant and contemporary feel to the design - yet it must be professional and sharp.

Target Market(s)

corporates

Industry/Entity Type

Finance

Colors
ffc214

Requirements
Must have
• an impactful first impression - that conjurs image of professionalism
Should not have
• cartoon

```html
<!DOCTYPE html>
<html lang="en">
<head>
<meta charset="utf-8">
<title>The Meridian Advisory – Entrance Sign</title>
<link rel="stylesheet" href="https://fonts.googleapis.com/css2?family=Cormorant+Garamond:wght@500&display=swap">
<style>
  :root {
    --page: #ffffff;
    --panel: #050707;
    --brand-blue: #2b64a3;
    --accent-orange: #ee6a2c;
    --curl-light: #ffffff;
    --curl-shade: #c9c9c9;
    --shadow: rgba(0,0,0,0.35);
  }
  html, body {
    margin: 0;
    padding: 0;
    width: 1200px;
    height: 2400px;
    overflow: hidden;
    background: var(--page);
  }
  .sign {
    position: relative;
    width: 1200px;
    height: 2400px;
  }
  .sign-layer {
    position: absolute;
    inset: 0;
    width: 1200px;
    height: 2400px;
  }
  .brand {
    position: absolute;
    left: 0;
    right: 0;
    top: 470px;
    display: flex;
    flex-direction: column;
    align-items: center;
  }
  .brand-square {
    width: 170px;
    height: 170px;
    background: var(--accent-orange);
  }
  .brand-name {
    margin: 250px 0 0;
    font-family: "Cormorant Garamond", serif;
    font-weight: 500;
    font-size: 92px;
    line-height: 1;
    letter-spacing: -0.5px;
    color: var(--brand-blue);
  }
  .motto {
    position: absolute;
    left: 0;
    right: 0;
    top: 2240px;
    margin: 0;
    text-align: center;
    font-family: "Cormorant Garamond", serif;
    font-weight: 500;
    font-size: 36px;
    letter-spacing: 0.62em;
    padding-left: 0.62em;
    color: var(--accent-orange);
  }
</style>
</head>
<body>
<main class="sign">
  <svg class="sign-layer panel-layer" viewBox="0 0 500 1000" aria-hidden="true">
    <path class="panel" fill="var(--panel)"
      d="M12,10 H488 V772 C440,822 300,885 200,987 H12 Z"/>
  </svg>

  <header class="brand">
    <div class="brand-square" aria-hidden="true"></div>
    <h1 class="brand-name">The Meridian Advisory</h1>
  </header>

  <p class="motto">ALWAYS ON THE SAME PAGE</p>

  <svg class="sign-layer curl-layer" viewBox="0 0 500 1000" aria-hidden="true">
    <defs>
      <linearGradient id="curlFace" x1="0.9" y1="0.1" x2="0.2" y2="0.9">
        <stop offset="0" stop-color="var(--curl-shade)"/>
        <stop offset="0.35" stop-color="var(--curl-light)"/>
        <stop offset="0.8" stop-color="var(--curl-light)"/>
        <stop offset="1" stop-color="#e6e6e6"/>
      </linearGradient>
      <filter id="curlShadow" x="-20%" y="-20%" width="140%" height="140%">
        <feDropShadow dx="-3" dy="3" stdDeviation="4" flood-color="var(--shadow)"/>
      </filter>
    </defs>
    <path class="page-curl" fill="url(#curlFace)" filter="url(#curlShadow)"
      d="M488,772 C482,760 468,756 456,766 C405,826 262,880 172,948 C158,962 172,986 200,987 C300,885 440,822 488,772 Z"/>
  </svg>
</main>
</body>
</html>
```